CalmVisit Homepage and Landing Pages

Please see detailed brief.

CalmVisit is Australia’s newest online therapy and mental health service. We allow patients from across australia to connect with Mental health practitioners from across Australia. Our mission is to remove the friction in gaining support for mental health related issues.

Number of Pages Required

1 page

Font styles to use
Sans Serif

Colors
33a6d7
0293ce
3277b5
0255a3
acd136
9bcb3c

Requirements
Must have
• Please see detailed brief.
Nice to have
• Please see detailed brief
Should not have

```html
<!DOCTYPE html>
<html lang="en">
<head>
<meta charset="utf-8">
<title>CalmVisit – Online Mental Health Care</title>
<link href="https://fonts.googleapis.com/css2?family=Lato:wght@300;400;700;900&family=Roboto:wght@400;500;700&display=swap" rel="stylesheet">
<style>
:root{
  --blue:#0b5bd6;
  --blue-mid:#2272d6;
  --sky:#1a9be6;
  --link:#1f6fd6;
  --dark:#333333;
  --darker:#1e1e1e;
  --black:#000;
  --grey-bg:#f3f3f3;
  --text:#333;
  --muted:#555;
  --white:#fff;
}
*{box-sizing:border-box;margin:0;padding:0}
html,body{width:1200px;height:3277px;overflow:hidden}
body{position:relative;font-family:"Lato",sans-serif;color:var(--text);background:var(--white)}
.abs{position:absolute}
.ph{position:absolute}
/* header */
.brand{display:flex;align-items:center;gap:12px;font-family:"Lato",sans-serif;font-weight:300;font-size:44px;color:#444}
.brand-dot{width:34px;height:34px;border-radius:50%;background:var(--blue)}
.top-contact{font-size:13px;color:#333;display:flex;gap:14px;align-items:center}
.social{display:flex;gap:6px}
.social span{width:22px;height:22px;background:var(--sky);border-radius:3px;display:block}
.btn{display:flex;align-items:center;justify-content:center;font-family:"Lato",sans-serif;font-weight:700;font-size:13px;color:var(--white);text-decoration:none}
.nav{position:absolute;left:0;top:111px;width:1200px;height:40px;background:var(--dark)}
.nav a{position:absolute;top:12px;color:var(--white);font-weight:700;font-size:13px;text-decoration:none}
.search{position:absolute;right:60px;top:0;width:43px;height:40px;background:var(--black)}
/* hero */
.hero{position:absolute;left:0;top:151px;width:1200px;height:483px;overflow:hidden}
.hero-photo{left:0;top:0;width:700px;height:483px;background:linear-gradient(135deg,#e6e1db,#c9c2ba 60%,#8f8a85)}
.hero-panel{left:0;top:0;width:1200px;height:483px;background:var(--blue);clip-path:polygon(582px 0,100% 0,100% 100%,442px 100%)}
.hero-man{left:950px;top:70px;width:250px;height:330px;background:linear-gradient(180deg,#c99c83,#2a2a2a 45%,#1c1c1c)}
.badge{left:932px;top:234px;width:128px;height:128px;border-radius:50%;background:var(--sky);border:6px solid #3c8fe8;color:var(--white);text-align:center;font-family:"Roboto",sans-serif;font-weight:700;line-height:1;z-index:2}
.hero-title{position:absolute;z-index:3;left:604px;top:16px;width:340px;color:var(--white);font-family:"Roboto",sans-serif}
.hero-title .kicker{font-size:40px;font-weight:500;line-height:46px;white-space:nowrap}
.hero-title .headline{font-size:57px;font-weight:700;line-height:60px;margin-top:2px;white-space:nowrap}
.hero-title .lead{font-family:"Lato",sans-serif;font-size:14px;line-height:19px;margin-top:10px;width:330px}
.hero-title .prompt{font-family:"Lato",sans-serif;font-size:16px;font-weight:700;color:#111;margin-top:6px}
.hero-band{left:0;top:400px;width:1200px;height:83px;background:var(--sky);clip-path:polygon(466px 0,100% 0,100% 100%,442px 100%)}
.field{position:absolute;z-index:3;left:607px;width:205px;height:33px;background:var(--white);font-size:12px;color:#666;padding:10px 10px}
/* about */
h2.section{font-family:"Roboto",sans-serif;font-weight:500;font-size:44px;color:#111}
.para{font-family:Arial,sans-serif;font-size:12.5px;line-height:20.5px;color:#444}
/* how */
.how{position:absolute;left:0;top:1119px;width:1200px;height:421px;background:#3a3a3a;overflow:hidden}
.how-photo{left:0;top:0;width:600px;height:421px;background:linear-gradient(160deg,#5d7a3a,#2e3b22 55%,#1f2a18);clip-path:polygon(0 0,548px 0,433px 100%,0 100%)}
.step{position:absolute;top:60px;width:163px;height:328px;background:var(--white);text-align:center}
.step-num{position:absolute;left:53px;top:-25px;width:56px;height:56px;border-radius:50%;background:var(--sky);border:4px solid var(--white);color:var(--white);font-family:"Roboto",sans-serif;font-weight:500;font-size:36px;line-height:48px}
.step h4{margin-top:42px;font-family:"Roboto",sans-serif;font-weight:500;font-size:14px;color:#111}
.step p{font-family:Arial,sans-serif;font-size:10px;line-height:11px;color:#666;margin-top:4px;padding:0 8px}
.phone{position:absolute;left:30px;top:105px;width:103px;height:200px;border-radius:12px;background:#2b2b2b;padding:12px 5px}
.phone div{width:100%;height:100%;background:linear-gradient(180deg,#eef4fb,#dfe9f5)}
.cta-band{position:absolute;left:0;top:1540px;width:1200px;height:124px;background:var(--blue-mid)}
/* services */
.services{position:absolute;left:0;top:1664px;width:1200px;height:667px;background:var(--grey-bg)}
.card{position:absolute;width:341px;height:196px;background:var(--white)}
.card svg{position:absolute;left:28px;top:40px}
.card h3{position:absolute;left:116px;top:34px;font-family:"Lato",sans-serif;font-weight:700;font-size:19px;color:#222}
.card p{position:absolute;left:116px;top:68px;width:200px;font-size:12.5px;line-height:19px;color:#555}
.card a{position:absolute;left:116px;top:136px;font-size:14px;color:var(--link);text-decoration:none}
.card.active{background:linear-gradient(135deg,#2f7be0,#1d5fcc)}
.card.active h3,.card.active p,.card.active a{color:var(--white)}
/* team */
.member{position:absolute;top:2513px;width:249px}
.member .photo{height:261px}
.member .plate{height:60px;background:#e8e8e8;position:relative}
.plate .dot{position:absolute;left:12px;top:14px;width:32px;height:32px;border-radius:50%;background:var(--blue)}
.plate b{position:absolute;left:63px;top:10px;font-family:"Roboto",sans-serif;font-weight:500;font-size:22px;color:#111}
.plate small{position:absolute;left:63px;top:37px;font-size:11px;color:#555}
.plate a{position:absolute;right:12px;top:40px;font-size:11px;color:var(--link);text-decoration:none}
/* footer */
.footer{position:absolute;left:0;top:2940px;width:1200px;height:302px;background:var(--darker);color:var(--white)}
.footer h5{position:absolute;top:56px;font-family:"Roboto",sans-serif;font-weight:500;font-size:19px}
.flink{position:absolute;font-size:13px}
.flink::before{content:"";display:inline-block;width:5px;height:5px;border-radius:50%;background:var(--sky);margin-right:8px;vertical-align:middle}
.news-thumb{position:absolute;left:613px;width:74px;height:74px;background:linear-gradient(135deg,#e9c9a9,#8fbf6f)}
.news-title{position:absolute;left:710px;width:128px;font-size:13px;line-height:20px}
.news-date{position:absolute;left:714px;font-size:12px;color:var(--sky)}
.contact-row{position:absolute;left:907px;font-size:13px;line-height:24px}
.copyright{position:absolute;left:0;top:3242px;width:1200px;height:35px;background:var(--black);color:var(--white);font-size:12px;text-align:center;line-height:35px}
</style>
</head>
<body>

<header>
  <div class="abs brand" style="left:60px;top:30px"><span class="brand-dot"></span>CalmVisit</div>
  <div class="abs top-contact" style="left:686px;top:14px">
    <span>&#9742; + (1800) 555 0142</span>
    <span>&#9993; hello@calmvisit-care.com</span>
    <span class="social"><span></span><span></span><span></span><span></span></span>
  </div>
  <a class="abs btn" href="#" style="left:913px;top:51px;width:85px;height:36px;background:var(--blue)">Log in</a>
  <a class="abs btn" href="#" style="left:1007px;top:51px;width:132px;height:36px;background:var(--sky)">Patient Sign up</a>
</header>

<nav class="nav">
  <a href="#" style="left:80px">HOME</a>
  <a href="#" style="left:172px">HOW IT WORKS</a>
  <a href="#" style="left:322px">OUR SERVICES</a>
  <a href="#" style="left:469px">MEET OUR TEAM</a>
  <a href="#" style="left:637px">FAQ</a>
  <a href="#" style="left:727px">TESTIMONIALS</a>
  <a href="#" style="left:884px">CONTACT US</a>
  <div class="search"><svg width="43" height="40" viewBox="0 0 43 40"><circle cx="20" cy="18" r="7" fill="none" stroke="#fff" stroke-width="2"/><line x1="25" y1="23" x2="30" y2="28" stroke="#fff" stroke-width="2"/></svg></div>
</nav>

<section class="hero">
  <div class="ph hero-photo" role="img" aria-label="Woman stretching on a yoga mat in a bright living room"></div>
  <div class="ph hero-panel"></div>
  <div class="ph hero-man" role="img" aria-label="Smiling male practitioner in a black shirt holding a clipboard"></div>
  <div class="ph badge"><div style="font-size:40px;margin-top:32px">100%</div><div style="font-size:28px;margin-top:4px">online</div></div>
  <div class="hero-title">
    <div class="kicker">Our mission is simple</div>
    <div class="headline">No travel<br>No Clinics</div>
    <div class="lead">The consultation can be conducted from wherever you feel most comfortable.</div>
    <div class="prompt">Find the help you need</div>
  </div>
  <div class="field" style="top:261px">Name</div>
  <div class="field" style="top:302px">Phone no</div>
  <a class="abs btn" href="#" style="z-index:3;left:607px;top:348px;width:205px;height:32px;background:var(--dark);font-size:14px">Book an Appointment</a>
  <div class="ph hero-band"></div>
  <div class="abs" style="left:489px;top:417px;color:#fff;font-family:Roboto,sans-serif;font-size:18px;line-height:24px">CalmVisit provides on demand access to highly<br>qualified physicians from across Australia.</div>
  <a class="abs btn" href="#" style="left:967px;top:428px;width:173px;height:36px;background:var(--dark)">Find a Practitioners</a>
</section>

<section>
  <h2 class="section abs" style="left:60px;top:708px">About Us</h2>
  <div class="abs" style="left:61px;top:762px;width:600px;color:var(--link);font-size:20px;line-height:26px">CalmVisit provides on-demand access to a range of psychologists &amp; personal wellness professionals from across Australia</div>
  <p class="abs para" style="left:59px;top:836px;width:585px">Employers must get to grip with mental health in the workplace with politicians focussing on the issue and recent case law showing that employers are failing to understand their responsibilitiesEmployers must get to grip with mental health in the workplace with politicians focussing on the issue and recent case law showing that employers are failing to understand their responsibilitiesEmployers must get to grip with mental health in the workplace with politicians focussing on the issue and recent case law showing that employers are failing to understand their responsibilities</p>
  <a class="abs btn" href="#" style="left:60px;top:1003px;width:165px;height:37px;background:var(--blue);font-weight:400;font-size:14px">Know More</a>
  <div class="ph" role="img" aria-label="Video still of a woman in a gym making a peace sign" style="left:684px;top:710px;width:455px;height:330px;background:linear-gradient(135deg,#d8d8d4,#a9a7a2 50%,#5a5753)"></div>
  <svg class="abs" style="left:874px;top:850px" width="90" height="90" viewBox="0 0 90 90"><circle cx="45" cy="45" r="40" fill="rgba(0,0,0,.35)" stroke="#fff" stroke-width="4"/><polygon points="36,28 64,45 36,62" fill="#fff"/></svg>
</section>

<section class="how">
  <div class="ph how-photo" role="img" aria-label="Woman in a dance pose stretching on grass in a park"></div>
  <div class="abs" style="left:300px;top:183px;width:293px;height:58px;background:var(--sky);color:#fff;font-family:Roboto,sans-serif;font-weight:500;font-size:41px;line-height:58px;padding-left:20px">How it works</div>
  <div class="step" style="left:607px"><div class="step-num">1</div><h4>Find a practitoner</h4><p>Search for health professional anywhere in Australia.</p><div class="phone"><div role="img" aria-label="App screen showing a practitioner profile"></div></div></div>
  <div class="step" style="left:793px"><div class="step-num">2</div><h4>Book an Appointment</h4><p>Book an online appointment at time that suits you.</p><div class="phone"><div role="img" aria-label="App screen showing a booking calendar"></div></div></div>
  <div class="step" style="left:977px"><div class="step-num">3</div><h4>Chat your consultant</h4><p>You have the option a voice only or video call.</p><div class="phone"><div role="img" aria-label="App screen showing a video call with a doctor"></div></div></div>
</section>

<section class="cta-band">
  <div class="abs" style="left:60px;top:22px;width:870px;color:#fff;font-family:Roboto,sans-serif;font-weight:500;font-size:20px;line-height:24.5px">CalmVisit allows GP's &amp; mental health practitioners from across Australia to connect and treat patients country wide.&nbsp; If you have over 10 years experience and a valid practicing license, sign up below and become a CalmVisit today anxiety.</div>
  <a class="abs btn" href="#" style="left:935px;top:44px;width:210px;height:38px;background:#fff;color:#111;font-family:Roboto,sans-serif;font-weight:500;font-size:17px">Sign up as Practitioners</a>
</section>

<section class="services">
  <h2 class="section abs" style="left:58px;top:66px">Our Services</h2>
  <p class="abs para" style="left:59px;top:116px;width:1080px;font-size:12px;line-height:16px">Osed quia consequuntur magni dolores eos qui ratione voluptatem sequi nesciunt. Neque porro quisquam est, qui dolorem ipsum quia dolor sit amet, consectetur, adipisci sed quia non numquam qui ratione voluptatem sequi nesciunt.</p>

  <div class="card active" style="left:57px;top:186px">
    <svg width="60" height="60" viewBox="0 0 60 60" fill="none" stroke="#fff" stroke-width="2.5" stroke-linecap="round"><circle cx="40" cy="10" r="5"/><path d="M20 22l12-6 8 10 10 2M32 16l-6 18 10 8-4 14M26 34l-10 10H6"/></svg>
    <h3>Balance Body mind</h3>
    <p>Lorem Ipsum is simply my text of the printing and Ipsum is simply text of the Ipsum is simply.</p>
    <a href="#">Read more</a>
  </div>
  <div class="card" style="left:424px;top:186px">
    <svg width="60" height="60" viewBox="0 0 60 60" fill="none" stroke="#1f6fd6" stroke-width="2.5" stroke-linecap="round"><path d="M18 4c4 10 4 18-2 28-4 8-2 20 2 24M42 4c-4 10-4 18 2 28 4 8 2 20-2 24M18 40h24M26 46l4 4 4-4"/></svg>
    <h3>Weight Loss Program</h3>
    <p>Lorem Ipsum is simply my text of the printing and Ipsum is simply text of the Ipsum is simply.</p>
    <a href="#">Read more</a>
  </div>
  <div class="card" style="left:793px;top:186px">
    <svg width="60" height="60" viewBox="0 0 60 60" fill="none" stroke="#1f6fd6" stroke-width="2.5" stroke-linejoin="round"><path d="M30 52C10 38 4 28 4 18 4 10 10 4 17 4c6 0 10 4 13 8 3-4 7-8 13-8 7 0 13 6 13 14 0 10-6 20-26 34z"/><path d="M6 28h14l4-8 6 16 5-10h19"/></svg>
    <h3>Cardio Excercise</h3>
    <p>Lorem Ipsum is simply my text of the printing and Ipsum is simply text of the Ipsum is simply.</p>
    <a href="#">Read more</a>
  </div>
  <div class="card" style="left:57px;top:410px">
    <svg width="60" height="60" viewBox="0 0 60 60" fill="none" stroke="#1f6fd6" stroke-width="2.5" stroke-linecap="round"><circle cx="40" cy="10" r="5"/><path d="M20 22l12-6 8 10 10 2M32 16l-6 18 10 8-4 14M26 34l-10 10H6"/></svg>
    <h3>Fitness &amp; Performance</h3>
    <p>Lorem Ipsum is simply my text of the printing and Ipsum is simply text of the Ipsum is simply.</p>
    <a href="#">Read more</a>
  </div>
  <div class="card" style="left:426px;top:410px">
    <svg width="60" height="60" viewBox="0 0 60 60" fill="none" stroke="#1f6fd6" stroke-width="2.5"><rect x="6" y="14" width="18" height="38" rx="4"/><path d="M10 14V6h10v8"/><circle cx="40" cy="40" r="13"/><path d="M40 27c0-6 4-10 8-10"/></svg>
    <h3>Nutrition Plan</h3>
    <p>Lorem Ipsum is simply my text of the printing and Ipsum is simply text of the Ipsum is simply.</p>
    <a href="#">Read more</a>
  </div>
  <div class="card" style="left:795px;top:410px">
    <svg width="60" height="60" viewBox="0 0 60 60" fill="none" stroke="#1f6fd6" stroke-width="2.5"><rect x="6" y="34" width="8" height="18" rx="2"/><rect x="46" y="34" width="8" height="18" rx="2"/><path d="M14 43h32"/><rect x="22" y="6" width="16" height="28" rx="3"/><path d="M26 2h8"/></svg>
    <h3>Routein Programe</h3>
    <p>Lorem Ipsum is simply my text of the printing and Ipsum is simply text of the Ipsum is simply.</p>
    <a href="#">Read more</a>
  </div>
</section>

<section>
  <h2 class="section abs" style="left:58px;top:2390px">Meet our Practitoners</h2>
  <p class="abs para" style="left:59px;top:2446px;font-size:12px">Our Practitioners are what makes CalmVisit tick.&nbsp; However behind every great product is a hardworking team ensuring that CalmVisit can deliver the highest quality of service.</p>
  <div class="member" style="left:61px"><div class="photo" role="img" aria-label="Portrait of a male fitness coach with a towel" style="background:linear-gradient(160deg,#8c8478,#4a5a6d)"></div><div class="plate"><span class="dot"></span><b>Daniel Marsh</b><small>Fitness Coach</small><a href="#">Join Now</a></div></div>
  <div class="member" style="left:337px"><div class="photo" role="img" aria-label="Portrait of a female weight loss coach running outdoors" style="background:linear-gradient(160deg,#a9a59b,#6d6a62 60%,#c46a6f)"></div><div class="plate"><span class="dot"></span><b>Lena Ortiz</b><small>Weight loss Coach</small><a href="#">Join Now</a></div></div>
  <div class="member" style="left:615px"><div class="photo" role="img" aria-label="Portrait of a smiling male fitness coach holding a clipboard" style="background:linear-gradient(160deg,#b8b8b4,#5a5a58 60%,#3a4a5c)"></div><div class="plate"><span class="dot"></span><b>Marcus Bell</b><small>Fitness Coach</small><a href="#">Join Now</a></div></div>
  <div class="member" style="left:891px"><div class="photo" role="img" aria-label="Portrait of a smiling female fitness coach with curly hair" style="background:linear-gradient(160deg,#7b8a62,#3e3a30 60%,#c9a184)"></div><div class="plate"><span class="dot"></span><b>Ivy Carter</b><small>Fitness Coach</small><a href="#">Join Now</a></div></div>
</section>

<footer class="footer">
  <div class="abs brand" style="left:70px;top:60px;font-size:34px;color:#fff;gap:10px"><span class="brand-dot" style="width:26px;height:26px"></span>CalmVisit</div>
  <p class="abs" style="left:70px;top:118px;width:245px;font-size:13px;line-height:26px">Your Transformation is our passion &amp; We are your personal trainers, trained nutritionist, your supplement experts, your health coach, your support group</p>

  <h5 style="left:340px">Quick Links</h5>
  <span class="flink" style="left:340px;top:108px">News &amp; Tips</span>
  <span class="flink" style="left:340px;top:141px">About Us</span>
  <span class="flink" style="left:340px;top:174px">Healthy Food</span>
  <span class="flink" style="left:340px;top:207px">Latest Events</span>
  <span class="flink" style="left:475px;top:108px">Coachers</span>
  <span class="flink" style="left:475px;top:141px">Our Shop</span>
  <span class="flink" style="left:475px;top:174px">Get Offers</span>
  <span class="flink" style="left:475px;top:207px">Contact Us</span>

  <h5 style="left:610px">Recent News</h5>
  <div class="news-thumb" style="top:104px" role="img" aria-label="Mother and child preparing a healthy meal"></div>
  <div class="news-title" style="top:100px">Stop Getting Annoyed If You Want Better Health</div>
  <div class="news-date" style="top:174px">June, 15 2017</div>
  <div class="news-thumb" style="top:206px" role="img" aria-label="Family enjoying fresh vegetables outdoors"></div>
  <div class="news-title" style="top:202px">What is a "Healthy" Food? The Answer Will Surprise You</div>
  <div class="news-date" style="top:276px">June, 15 2017</div>

  <h5 style="left:879px">Contact Us</h5>
  <svg class="abs" style="left:879px;top:110px" width="18" height="18" viewBox="0 0 18 18" fill="none" stroke="#1a9be6" stroke-width="1.6"><path d="M3 2l4 1 1 4-2 1c1 2 3 4 5 5l1-2 4 1 1 4c-8 1-15-6-14-14z"/></svg>
  <div class="contact-row" style="top:106px"><b>Phone:</b> +123-555-0199</div>
  <svg class="abs" style="left:879px;top:146px" width="18" height="18" viewBox="0 0 18 18" fill="none" stroke="#1a9be6" stroke-width="1.6"><rect x="1" y="4" width="16" height="11"/><path d="M1 4l8 6 8-6"/></svg>
  <div class="contact-row" style="top:142px"><b>Email:</b> care@calmvisit-mail.com</div>
  <svg class="abs" style="left:881px;top:180px" width="16" height="20" viewBox="0 0 16 20" fill="none" stroke="#1a9be6" stroke-width="1.6"><path d="M8 19S2 11 2 7a6 6 0 0112 0c0 4-6 12-6 12z"/><circle cx="8" cy="7" r="2"/></svg>
  <div class="contact-row" style="top:176px;width:230px"><b>Address:</b> Willow Rd, Brookfield NSW 2040, AU</div>
</footer>

<div class="abs" style="left:60px;top:2889px;width:1080px;height:79px;background:var(--sky)">
  <div class="abs" style="left:30px;top:20px;color:#fff;font-family:Roboto,sans-serif;font-weight:500;font-size:29px">Find out latest news &amp; offers</div>
  <div class="abs" style="left:439px;top:25px;width:444px;height:33px;border:1px solid #cfe9fa;color:#fff;font-size:12px;padding:9px 12px">Email Address</div>
  <a class="abs btn" href="#" style="left:920px;top:25px;width:122px;height:33px;background:#fff;color:#111;font-weight:400">Submit Now</a>
</div>

<div class="copyright">Copyright © calmvisit2020. All rights reserved</div>

</body>
</html>
```